Games for Classrooms Website Redesign

The purpose of the website redesign is to freshen up the content and update it to give a more modern look and feel. It will show what we do concisely and satisfy all potential visitors. We work with primary schools and the brand is fun.About: Games for Classrooms is a scheme that brings top Olympic athletes into primary schools to inspire children to do more physical activity. We typically run a half day event at the school where the athlete does a fun fitness circuit with the children and then an inspirational assembly with a demonstration and Q&A. The children are asked to collect sponsorship money to take part in the event and a large proportion of the money raised goes back to the school in the form of a voucher for them to spend on new sports equipment. 1. To generate more leads from potential customers/schools2. To engage the children and parents more in the event and get them excited for their upcoming visit whilst setting up a fundraiser page.3. To simplify and modernise what is already there.

I have attached some ideas for each of the pages (uploaded in brief)

Here is a link to our current website: www.gamesforclassrooms.org

I have also attached a link to the sponsorship form which shows the kind of look and feel we're after.

Target Market(s)

Primary school teachers
Primary school parents

Number of Pages Required

5+ page

Requirements
Must have
• Fun, modern.
• Be built on twitter bootstrap

```html
<!DOCTYPE html>
<html lang="en">
<head>
<meta charset="utf-8">
<title>Games for Classrooms — Home</title>
<link rel="stylesheet" href="https://fonts.googleapis.com/css2?family=Montserrat:wght@600;700;800;900&display=swap">
<style>
  :root {
    --white: #ffffff;
    --ink: #111111;
    --rule: #ececec;
    --red: #e3182d;
    --blue: #1d9ae6;
    --green: #5cc43a;
    --quote-blue: #cfe7fa;
    --photo-warm: #7a4a36;
    --photo-mid: #b58a6a;
    --photo-yellow: #e9b824;
  }
  * { margin: 0; padding: 0; box-sizing: border-box; }
  html, body { width: 1200px; height: 626px; overflow: hidden; background: var(--white); }
  body { font-family: "Montserrat", Arial, sans-serif; color: var(--ink); }

  .site { width: 1200px; height: 626px; position: relative; }

  .site-header {
    height: 60px; display: flex; align-items: center; justify-content: space-between;
    padding: 0 70px; border-bottom: 1px solid var(--rule);
  }
  .brand { display: flex; align-items: center; gap: 8px; font-weight: 800; font-size: 13px; color: var(--red); text-transform: uppercase; letter-spacing: .3px; }
  .brand-dot { width: 14px; height: 14px; border-radius: 50%; background: var(--red); }
  .menu-toggle { display: flex; align-items: center; gap: 10px; font-weight: 700; font-size: 11px; letter-spacing: 1px; }
  .menu-lines { display: flex; flex-direction: column; gap: 3px; }
  .menu-lines span { display: block; width: 22px; height: 2px; }
  .menu-lines span:nth-child(1) { background: var(--red); }
  .menu-lines span:nth-child(2) { background: var(--green); }
  .menu-lines span:nth-child(3) { background: var(--blue); }

  .mission { height: 180px; position: relative; display: flex; align-items: center; justify-content: center; }
  .quote-mark {
    position: absolute; font-family: Georgia, "Times New Roman", serif; font-weight: 700;
    font-size: 190px; line-height: 1; color: var(--quote-blue); user-select: none;
  }
  .quote-mark--open { left: 430px; top: 2px; }
  .quote-mark--close { left: 680px; top: 60px; }
  .mission-text {
    position: relative; width: 440px; text-align: center; font-weight: 800; font-size: 18px;
    line-height: 1.2; letter-spacing: 1.2px; text-transform: uppercase;
  }

  .hero-photo {
    height: 210px;
    background: linear-gradient(90deg, var(--photo-warm) 0%, var(--photo-mid) 35%, var(--photo-yellow) 50%, var(--photo-mid) 68%, var(--photo-warm) 100%);
  }

  .audience { height: 175px; display: flex; justify-content: center; align-items: center; gap: 260px; }
  .audience-button {
    position: relative; width: 124px; height: 124px; border-radius: 50%;
    display: flex; align-items: center; justify-content: center; text-align: center;
    color: var(--white); font-weight: 800; font-size: 14px; line-height: 1.15; text-transform: uppercase;
    text-decoration: none;
  }
  .audience-button::before {
    content: ""; position: absolute; inset: -2px 4px 4px -6px; border: 2px solid var(--ink); border-radius: 50%;
  }
  .audience-button--school { background: var(--red); }
  .audience-button--parent { background: var(--blue); }
</style>
</head>
<body>
<div class="site">
  <header class="site-header">
    <div class="brand"><span class="brand-dot"></span>Games for Classrooms</div>
    <div class="menu-toggle">
      <div class="menu-lines"><span></span><span></span><span></span></div>
      MENU
    </div>
  </header>

  <section class="mission">
    <span class="quote-mark quote-mark--open" aria-hidden="true">&ldquo;</span>
    <span class="quote-mark quote-mark--close" aria-hidden="true">&rdquo;</span>
    <p class="mission-text">Our mission is to put physical health in children on a par with mental health and academic excellence.</p>
  </section>

  <div class="hero-photo" role="img" aria-label="Photo of smiling primary school children in bright red and yellow sports shirts at an assembly"></div>

  <section class="audience">
    <a class="audience-button audience-button--school" href="#">I'm a<br>school</a>
    <a class="audience-button audience-button--parent" href="#">I'm a<br>parent</a>
  </section>
</div>
</body>
</html>
```